New business outdoor sign design

We want to update our current Hotel sign to be modern design. We are open to ideas. The file that we upload is the size of the sign the blue sign is what we have now. We want completely new face look. Also there is also a backlight behind the face of the sign. Only words on sign we want is (4 Bells) we do not want the hotel part there. The sign company ask that it is done in vector art form. The design does NOT have to have a tree, we are open to all ideas, font styles. Be creative
Just a reminder the design does not have to have a tree, and you can use any font style. We are very open to any type of design.

```html
<!DOCTYPE html>
<html lang="en">
<head>
<meta charset="utf-8">
<title>4 Bells – Sign Concept 02</title>
<link rel="stylesheet" href="https://fonts.googleapis.com/css2?family=Poppins:wght@700&family=Source+Sans+3:wght@400&display=swap">
<style>
  :root {
    --backdrop: #e4e4e4;
    --sign-face: #ffffff;
    --border-pattern: #f4f3ee;
    --border-pattern-edge: #ebe9e0;
    --panel: #535355;
    --panel-edge: #6ca824;
    --brand-green: #6ca824;
    --shadow: #a9a9a9;
    --caption: #555555;
  }
  html, body {
    margin: 0;
    padding: 0;
    width: 1200px;
    height: 743px;
    overflow: hidden;
    background: var(--backdrop);
  }
  .canvas {
    position: relative;
    width: 1200px;
    height: 743px;
  }
  .sign {
    position: absolute;
    left: 0;
    top: 0;
    width: 1200px;
    height: 743px;
  }
  .sign__shadow { fill: var(--shadow); }
  .sign__border { fill: url(#borderTone); }
  .sign__panel {
    fill: var(--panel);
    stroke: var(--panel-edge);
    stroke-width: 1;
  }
  .sign__name {
    font-family: "Poppins", sans-serif;
    font-weight: 700;
    font-size: 196px;
    fill: var(--brand-green);
    letter-spacing: -2px;
  }
  .caption {
    position: absolute;
    left: 0;
    width: 1200px;
    top: 647px;
    margin: 0;
    text-align: center;
    font-family: "Source Sans 3", sans-serif;
    font-weight: 400;
    font-size: 15px;
    letter-spacing: 0.2px;
    color: var(--caption);
  }
</style>
</head>
<body>
<main class="canvas">
  <svg class="sign" viewBox="0 0 1200 743" xmlns="http://www.w3.org/2000/svg">
    <defs>
      <linearGradient id="borderTone" x1="0" y1="0" x2="1" y2="1">
        <stop offset="0" stop-color="var(--border-pattern)"/>
        <stop offset="0.5" stop-color="var(--sign-face)"/>
        <stop offset="1" stop-color="var(--border-pattern-edge)"/>
      </linearGradient>
    </defs>

    <rect class="sign__shadow" x="119" y="97" width="978" height="520"/>
    <rect class="sign__border" x="111" y="89" width="978" height="520"
          role="img" aria-label="Faint interlocking geometric line pattern framing the sign face"/>

    <path class="sign__panel"
          d="M200,144 H1000 A33,33 0 0 0 1033,177 V521 A33,33 0 0 0 1000,554 H200 A33,33 0 0 0 167,521 V177 A33,33 0 0 0 200,144 Z"/>

    <text class="sign__name" x="600" y="427" text-anchor="middle">4 Bells</text>
  </svg>

  <p class="caption">Design concept 4 Bells Sign 02</p>
</main>
</body>
</html>
```